Conference banner for Kestrel training organisation

We empower everyday heroes.
We provide training that empowers individuals to create positive change in themselves, their community, and the world.
We need a large banner design to promote the organisation at conferences and events. We are open to ideas and creativity.
It may involve creatively displaying our logo only, or it may involve our logo and a summary of our products (Kestrel training, Calm Minds Field Care).
Size: 820mm width x 1790mm height
300dpi
Target Market(s)
Educators and frontline health, community, and social workers.
Industry/Entity Type
Training
Colors
Designer to choose colors to be used in the design.

```html
<!DOCTYPE html>
<html lang="en">
<head>
<meta charset="utf-8">
<title>Kestrel Town – Conference Banner</title>
<link href="https://fonts.googleapis.com/css2?family=Montserrat:wght@800&family=Questrial&display=swap" rel="stylesheet">
<style>
  :root {
    --canvas: #ffffff;
    --sky-light: #fdecc0;
    --sky-warm: #f8d597;
    --band-green: #83c99a;
    --band-text: #fdf6dd;
    --brand-blue: #3d8fd8;
    --sun-light: #fcd994;
    --sun-mid: #f8ae5c;
    --sun-deep: #c26c33;
    --emblem-tone: #d9a27a;
  }
  html, body {
    margin: 0;
    padding: 0;
    width: 1000px;
    height: 1200px;
    overflow: hidden;
    background: var(--canvas);
  }
  .banner {
    position: relative;
    width: 1000px;
    height: 1200px;
  }
  .banner-panels {
    position: absolute;
    inset: 0;
  }
  .brand-name {
    position: absolute;
    left: 226px;
    width: 548px;
    top: 92px;
    margin: 0;
    text-align: center;
    font-family: "Montserrat", sans-serif;
    font-weight: 800;
    color: var(--brand-blue);
    font-size: 96px;
    line-height: 112px;
    letter-spacing: 0;
  }
  .program-band {
    position: absolute;
    left: 226px;
    width: 548px;
    top: 450px;
    height: 128px;
    display: flex;
    flex-direction: column;
    align-items: center;
    justify-content: center;
    font-family: "Questrial", sans-serif;
    color: var(--band-text);
    text-transform: uppercase;
  }
  .program-title {
    margin: 0;
    font-size: 50px;
    line-height: 54px;
    letter-spacing: 1px;
  }
  .program-subtitle {
    margin: 2px 0 0;
    font-size: 36px;
    line-height: 38px;
    letter-spacing: 1px;
  }
  .emblem {
    position: absolute;
    left: 284px;
    top: 656px;
    width: 432px;
    height: 484px;
  }
  .emblem-name {
    font-family: "Questrial", sans-serif;
    font-size: 40px;
    letter-spacing: 2px;
    fill: var(--band-text);
  }
</style>
</head>
<body>
<main class="banner">
  <svg class="banner-panels" width="1000" height="1200" viewBox="0 0 1000 1200" aria-hidden="true">
    <defs>
      <linearGradient id="sky" x1="0" y1="0" x2="0.3" y2="1">
        <stop offset="0" stop-color="var(--sky-light)"/>
        <stop offset="1" stop-color="var(--sky-warm)"/>
      </linearGradient>
      <linearGradient id="sun" x1="1" y1="0" x2="0" y2="1">
        <stop offset="0" stop-color="var(--sun-light)"/>
        <stop offset="0.55" stop-color="var(--sun-mid)"/>
        <stop offset="1" stop-color="var(--sun-deep)"/>
      </linearGradient>
    </defs>
    <path d="M226 2 H774 V442 L226 432 Z" fill="url(#sky)"/>
    <path d="M226 432 Q250 200 330 2 L226 2 Z" fill="#f9d9a0" opacity="0.45"/>
    <path d="M360 434 Q420 180 560 2 L600 2 Q460 190 400 435 Z" fill="#fff3d6" opacity="0.35"/>
    <rect x="226" y="450" width="548" height="128" fill="var(--band-green)"/>
    <path d="M226 584 L774 598 V1198 H226 Z" fill="url(#sun)"/>
    <path d="M226 1198 Q560 1080 774 900 V1198 Z" fill="#fde3a6" opacity="0.22"/>
    <path d="M300 600 Q260 850 300 1198 L226 1198 V600 Z" fill="#f7b463" opacity="0.25"/>
  </svg>

  <h1 class="brand-name">KESTREL<br>TOWN</h1>

  <section class="program-band">
    <p class="program-title">Kestrel Training</p>
    <p class="program-subtitle">Calm Minds Field Care</p>
  </section>

  <svg class="emblem" role="img" aria-label="Kestrel Town emblem: name mark in faint tone" width="432" height="484" viewBox="0 0 432 484">
    <circle cx="216" cy="200" r="150" fill="var(--emblem-tone)" opacity="0.45"/>
    <text class="emblem-name" x="216" y="214" text-anchor="middle">KESTREL TOWN</text>
  </svg>
</main>
</body>
</html>
```